TalkBloom - Language Coaching Services

Sleek, innovative, trendy design for Language Coaching business.

TalkBloom is a new UK based company that provides Language Coaching services. We offer highly personalized on-line and face to face language courses. We also impart learning techniques workshops based on the latest neuroscience research for second-language acquisition.

Target Market(s)

Industry/Entity Type

Consulting

Contact Information for Business Card

TalkBloom
DaniraQT@talkbloom.co.uk
TalkBloom.co.uk
London, UK

Font styles to use
Sans Serif

```html
<!DOCTYPE html>
<html lang="en">
<head>
<meta charset="utf-8">
<title>TalkBloom – Business Card</title>
<link rel="stylesheet" href="https://fonts.googleapis.com/css2?family=Montserrat:wght@400;500;600&display=swap">
<style>
  :root {
    --page: #ecebe8;
    --card-dark: #2d2e31;
    --card-edge: #c9cbcc;
    --brand-blue: #1b8fc9;
    --band-blue: #2f8fb8;
    --panel-warm: #d9a56f;
    --panel-cool: #4f90ae;
  }
  * { margin: 0; padding: 0; box-sizing: border-box; }
  html, body {
    width: 1000px;
    height: 1200px;
    overflow: hidden;
    background: var(--page);
    font-family: "Montserrat", Arial, sans-serif;
  }
  .card {
    position: absolute;
    left: 216px;
    width: 640px;
    height: 366px;
    background: var(--card-dark);
    border: 1px solid var(--card-edge);
    overflow: hidden;
    box-shadow: 0 6px 18px rgba(0, 0, 0, 0.18);
  }
  .card--front { top: 112px; }
  .card--back  { top: 716px; }

  .symbol-field {
    position: absolute;
    inset: 0;
    width: 640px;
    height: 366px;
  }

  .brand {
    position: absolute;
    display: flex;
    flex-direction: column;
    align-items: center;
    color: var(--brand-blue);
  }
  .brand__circle {
    border: 4px solid var(--brand-blue);
    border-radius: 50%;
  }
  .brand__name {
    font-weight: 500;
    text-transform: uppercase;
    letter-spacing: 1.5px;
    line-height: 1;
  }
  .card--front .brand { left: 26px; top: 106px; width: 250px; }
  .card--front .brand__circle { width: 98px; height: 98px; margin-bottom: 14px; }
  .card--front .brand__name { font-size: 32px; }

  .card--back .brand { right: 22px; top: 22px; width: 240px; }
  .card--back .brand__circle { width: 80px; height: 80px; margin-bottom: 14px; }
  .card--back .brand__name { font-size: 29px; }

  .person {
    position: absolute;
    right: 24px;
    top: 182px;
    text-align: right;
    color: var(--brand-blue);
  }
  .person__name { font-size: 19px; font-weight: 600; line-height: 1.3; }
  .person__role { font-size: 16px; font-weight: 500; line-height: 1.4; }

  .contacts {
    position: absolute;
    right: 24px;
    top: 250px;
    list-style: none;
    color: var(--brand-blue);
    font-size: 15px;
    font-weight: 500;
  }
  .contacts li {
    display: flex;
    justify-content: flex-end;
    align-items: center;
    gap: 12px;
    height: 24px;
  }
  .contacts svg { width: 16px; height: 16px; fill: var(--brand-blue); }
</style>
</head>
<body>

<section class="card card--front" aria-label="Business card front">
  <svg class="symbol-field" viewBox="0 0 640 366" role="img" aria-label="Large brand symbol decoration area">
    <defs>
      <linearGradient id="front-field" x1="0" y1="0" x2="1" y2="1">
        <stop offset="0" stop-color="#e2b07a"/>
        <stop offset="0.55" stop-color="#c89a6c"/>
        <stop offset="1" stop-color="#5f8fa6"/>
      </linearGradient>
    </defs>
    <path d="M330 0 C 300 90, 285 160, 300 230 C 312 290, 360 330, 370 366 L640 366 L640 0 Z" fill="url(#front-field)"/>
    <path d="M330 0 C 300 90, 285 160, 300 230 C 312 290, 360 330, 370 366" fill="none" stroke="var(--band-blue)" stroke-width="22" stroke-opacity="0.75"/>
  </svg>
  <div class="brand">
    <span class="brand__circle"></span>
    <span class="brand__name">TalkBloom</span>
  </div>
</section>

<section class="card card--back" aria-label="Business card back">
  <svg class="symbol-field" viewBox="0 0 640 366" role="img" aria-label="Large brand symbol decoration area">
    <defs>
      <linearGradient id="back-field" x1="0" y1="0" x2="1" y2="1">
        <stop offset="0" stop-color="#e2b07a"/>
        <stop offset="0.6" stop-color="#c89a6c"/>
        <stop offset="1" stop-color="#5f8fa6"/>
      </linearGradient>
    </defs>
    <path d="M0 0 L200 0 C 280 40, 320 110, 325 180 C 330 250, 280 320, 270 366 L0 366 Z" fill="url(#back-field)"/>
    <path d="M200 0 C 280 40, 320 110, 325 180 C 330 250, 280 320, 270 366" fill="none" stroke="var(--band-blue)" stroke-width="22" stroke-opacity="0.75"/>
  </svg>
  <div class="brand">
    <span class="brand__circle"></span>
    <span class="brand__name">TalkBloom</span>
  </div>
  <div class="person">
    <p class="person__name">Danira Quinn Talbot</p>
    <p class="person__role">Director</p>
  </div>
  <ul class="contacts">
    <li>+44(0)7700 900418
      <svg viewBox="0 0 16 16" aria-hidden="true"><path d="M2 6c0-2 3-3 6-3s6 1 6 3v1h-3V5.5C10 5 6 5 5 5.5V7H2z"/><rect x="4" y="8" width="8" height="6" rx="1"/></svg>
    </li>
    <li>DaniraQT@talkbloom.co.uk
      <svg viewBox="0 0 16 16" aria-hidden="true"><path d="M1 3h14v10H1z M2.5 4.5 8 9l5.5-4.5" fill="none" stroke="#1b8fc9" stroke-width="1.6"/></svg>
    </li>
    <li>www.TalkBloom.co.uk
      <svg viewBox="0 0 16 16" aria-hidden="true"><circle cx="8" cy="8" r="6.5" fill="none" stroke="#1b8fc9" stroke-width="1.6"/><path d="M1.5 8h13M8 1.5c3 3.5 3 9.5 0 13M8 1.5c-3 3.5-3 9.5 0 13" fill="none" stroke="#1b8fc9" stroke-width="1.2"/></svg>
    </li>
    <li>London, UK
      <svg viewBox="0 0 16 16" aria-hidden="true"><path d="M8 1a5 5 0 0 0-5 5c0 4 5 9 5 9s5-5 5-9a5 5 0 0 0-5-5zm0 7a2 2 0 1 1 0-4 2 2 0 0 1 0 4z"/></svg>
    </li>
  </ul>
</section>

</body>
</html>
```